Business Card Design with a glossy effect please

We supply and install Glass pool fencing: in Frameless, Semi Frameless, and Stainless Steel we also install Glass Balustrading, interior and exterior, plus Aluminium Tubular and Gates and Screens, and Quorix QT2240 Glass protection

Business

Dale Moreton
M 0432918506 or T 08 9517 3264
Unit 3 / 41 Lindale Crescent, Brenton Heights 6072
ABN: 51847203916
www.vistone-ky-poolfencing.com.au
info@vistone-ky-poolfencing.com.au

```html
<!DOCTYPE html>
<html lang="en">
<head>
<meta charset="utf-8">
<title>Vistone KY Pool Fencing — Business Cards</title>
<link href="https://fonts.googleapis.com/css2?family=Ubuntu:wght@400;500;700&display=swap" rel="stylesheet">
<style>
  :root {
    --page: #e9ecef;
    --white: #ffffff;
    --navy: #0d3f7a;
    --navy-deep: #082c5c;
    --blue: #1d74c4;
    --sky: #3fb9e6;
    --sky-light: #9fdcf3;
    --ink: #1b3f72;
    --muted: #5c86b3;
    --band-text: #cfe6fb;
  }
  * { box-sizing: border-box; margin: 0; padding: 0; }
  html, body {
    width: 1200px; height: 1023px; overflow: hidden;
    background: var(--page);
    font-family: "Ubuntu", sans-serif;
  }
  .stage {
    width: 1200px; height: 1023px;
    display: flex; align-items: center; justify-content: center; gap: 40px;
  }
  .card {
    position: relative; width: 540px; height: 330px; overflow: hidden;
    border-radius: 4px;
    box-shadow: 0 10px 30px rgba(8, 44, 92, 0.25);
  }

  /* Front */
  .card--front { background: var(--white); }
  .front__rule {
    position: absolute; left: 0; right: 0; top: 30px; height: 2px;
    background: var(--sky-light);
  }
  .front__glass {
    position: absolute; right: 0; top: 32px; width: 300px; height: 238px;
    background: linear-gradient(160deg, var(--sky-light) 0%, var(--sky) 55%, var(--blue) 100%);
    clip-path: polygon(35% 0, 100% 0, 100% 100%, 0 100%, 0 55%);
  }
  .front__band {
    position: absolute; left: 0; right: 0; bottom: 0; height: 60px;
    background: linear-gradient(180deg, var(--navy) 0%, var(--navy-deep) 100%);
    display: flex; align-items: center; justify-content: flex-end; padding-right: 26px;
    color: var(--band-text); font-size: 14px; letter-spacing: 0.2px;
  }
  .brand {
    position: absolute; left: 28px; top: 62px;
    display: flex; align-items: center; gap: 12px;
  }
  .brand__mark { width: 18px; height: 18px; background: var(--sky); }
  .brand__name {
    color: var(--navy); font-weight: 500; font-size: 26px; line-height: 1.05;
    letter-spacing: 0.5px; text-transform: uppercase;
  }
  .person {
    position: absolute; left: 30px; top: 150px;
    color: var(--ink); font-size: 18px; font-variant: small-caps; letter-spacing: 0.5px;
  }
  .person__role {
    font-variant: normal; font-size: 12px; color: var(--muted);
    border-left: 1px solid var(--muted); padding-left: 8px; margin-left: 6px;
  }
  .phones {
    position: absolute; left: 30px; top: 196px; list-style: none;
    color: var(--muted); font-size: 13px;
  }
  .online {
    position: absolute; right: 22px; top: 140px; list-style: none;
    color: var(--white); font-size: 12px;
  }
  .contact-line { display: flex; align-items: center; gap: 8px; margin-bottom: 8px; }
  .contact-line svg { width: 12px; height: 12px; flex: none; }

  /* Back */
  .card--back {
    background: linear-gradient(135deg, var(--navy) 0%, var(--navy-deep) 60%, var(--navy) 100%);
  }
  .back__band {
    position: absolute; left: 0; right: 0; top: 82px; height: 166px;
    background: var(--white);
    display: flex; flex-direction: column; align-items: center; justify-content: center; gap: 18px;
  }
  .back__line { position: absolute; left: 0; right: 0; height: 1px; background: var(--blue); }
  .back__line--top { top: 66px; }
  .back__line--bottom { bottom: 66px; }
  .card--back .brand { position: static; }
  .brand--large .brand__name { font-size: 30px; }
  .abn { color: var(--muted); font-size: 12px; letter-spacing: 0.5px; }
</style>
</head>
<body>
<main class="stage">
  <section class="card card--front" aria-label="Business card front">
    <div class="front__rule"></div>
    <div class="front__glass"></div>
    <div class="brand">
      <span class="brand__mark"></span>
      <span class="brand__name">Vistone KY<br>Pool Fencing</span>
    </div>
    <p class="person">Dale Moreton<span class="person__role">Director</span></p>
    <ul class="phones">
      <li class="contact-line">
        <svg viewBox="0 0 12 12"><rect x="3" y="0.5" width="6" height="11" rx="1" fill="none" stroke="currentColor"/><circle cx="6" cy="9.5" r="0.7" fill="currentColor"/></svg>
        043 291 8506
      </li>
      <li class="contact-line">
        <svg viewBox="0 0 12 12"><path d="M2.5 1.5 L4.5 1.5 L5.3 4 L4 5 Q5 7 7 8 L8 6.7 L10.5 7.5 L10.5 9.5 Q5.5 10.5 2 4 Z" fill="currentColor"/></svg>
        08 9517 3264
      </li>
    </ul>
    <ul class="online">
      <li class="contact-line">
        <svg viewBox="0 0 12 12"><rect x="0.5" y="2" width="11" height="8" fill="none" stroke="currentColor"/><path d="M0.5 2 L6 6.5 L11.5 2" fill="none" stroke="currentColor"/></svg>
        info@vistone-ky-poolfencing.com.au
      </li>
      <li class="contact-line">
        <svg viewBox="0 0 12 12"><circle cx="6" cy="6" r="5.3" fill="none" stroke="currentColor"/><path d="M0.7 6 H11.3 M6 0.7 Q2.5 6 6 11.3 M6 0.7 Q9.5 6 6 11.3" fill="none" stroke="currentColor"/></svg>
        www.vistone-ky-poolfencing.com.au
      </li>
    </ul>
    <footer class="front__band">Unit 3 / 41 Lindale Crescent, Brenton Heights 6072</footer>
  </section>

  <section class="card card--back" aria-label="Business card back">
    <div class="back__line back__line--top"></div>
    <div class="back__band">
      <div class="brand brand--large">
        <span class="brand__mark"></span>
        <span class="brand__name">Vistone KY<br>Pool Fencing</span>
      </div>
      <p class="abn">ABN: 51847203916</p>
    </div>
    <div class="back__line back__line--bottom"></div>
  </section>
</main>
</body>
</html>
```